Stationery design for law/Property/finance business

We need stationery design for a Law/Property/Finance business called Ridgemoor. Logo is attached.
we require a letterhead and with compliments slip.
Would like to see a very simple professional design using the colours of the logo and offset against Charcoal colours. Maybe a charcoal band for header and footer with logo and details appearing in it? Former letterhead attached for examples.
we require the project to be provided in word, pdf and jpeg format.
we require the following details on the stationery:
Harlow Bay Phone: 07 40551926
Tessford Phone: 07 40613847
Mobile: 0491 570 384
Fax: 07 40338172
email: admin@ridgemoorholdings-example.com.au
ABN 51 824 306 917

```html
<!DOCTYPE html>
<html lang="en">
<head>
<meta charset="utf-8">
<title>Ridgemoor Stationery</title>
<link href="https://fonts.googleapis.com/css2?family=Didact+Gothic&family=Parisienne&display=swap" rel="stylesheet">
<style>
  :root {
    --charcoal: #39393d;
    --charcoal-deep: #2c2c30;
    --teal: #7fd0c6;
    --blue: #2d76bd;
    --cyan: #34a5dc;
    --paper: #ffffff;
    --paper-shade: #f1f2f4;
    --ink: #55565a;
    --stage: #e6e8eb;
  }
  * { box-sizing: border-box; margin: 0; padding: 0; }
  html, body { width: 1200px; height: 1200px; overflow: hidden; }
  body {
    background: var(--stage);
    font-family: "Didact Gothic", "Century Gothic", sans-serif;
    color: var(--ink);
    position: relative;
  }
  .piece { position: absolute; background: var(--paper); box-shadow: 0 6px 18px rgba(0,0,0,.18); overflow: hidden; }
  .stripe { display: flex; height: 8px; flex: none; }
  .stripe span { flex: 1; }
  .stripe .s1 { background: var(--teal); }
  .stripe .s2 { background: var(--blue); }
  .stripe .s3 { background: var(--cyan); }
  .band { background: var(--charcoal); color: #cfd1d4; }
  .brand { display: flex; align-items: center; gap: 8px; color: var(--cyan); letter-spacing: .02em; text-transform: uppercase; white-space: nowrap; }
  .brand-dot { border-radius: 50%; background: var(--cyan); flex: none; }

  /* Letterhead */
  .letterhead { left: 620px; top: 60px; width: 540px; height: 764px; display: flex; flex-direction: column; }
  .letterhead .head { height: 92px; display: flex; justify-content: space-between; align-items: center; padding: 0 24px; }
  .letterhead .brand { font-size: 24px; }
  .letterhead .brand-dot { width: 18px; height: 18px; }
  .contact { font-size: 8.5px; line-height: 1.45; text-align: left; color: #d6d8db; white-space: nowrap; }
  .letter-body { flex: 1; padding: 110px 44px 20px; font-size: 10.5px; line-height: 1.55; }
  .letter-body .greeting { font-size: 15px; margin-bottom: 14px; }
  .letter-body p { margin-bottom: 14px; }
  .sign-off { font-size: 13px; line-height: 1.4; margin-top: 20px; }
  .signature { width: 150px; height: 36px; margin-top: 10px; background: linear-gradient(90deg, #e8e9eb, #f6f6f7); }
  .letterhead .foot { height: 34px; display: flex; align-items: center; justify-content: flex-end; padding: 0 24px; font-size: 11px; }

  /* Compliments slip */
  .slip { left: 40px; top: 60px; width: 550px; height: 255px; display: flex; flex-direction: column; }
  .slip .head { height: 58px; display: flex; align-items: center; justify-content: space-between; padding: 0 20px; }
  .slip .brand { font-size: 18px; }
  .slip .brand-dot { width: 13px; height: 13px; }
  .slip .script { font-family: "Parisienne", cursive; font-size: 26px; color: var(--teal); }
  .slip .field { flex: 1; background: linear-gradient(180deg, var(--paper), var(--paper-shade)); }
  .slip .foot { height: 40px; display: flex; align-items: center; justify-content: flex-end; padding: 0 20px; font-size: 10px; }

  /* Business cards */
  .card { width: 270px; height: 172px; top: 345px; }
  .card-front { left: 40px; display: flex; flex-direction: column; }
  .card-front .head { height: 54px; padding: 10px 14px; flex: none; }
  .card-front .name { font-size: 12px; color: var(--cyan); text-transform: uppercase; }
  .card-front .role { font-size: 8px; color: #c8cacd; margin-top: 2px; }
  .card-front .body { flex: 1; display: flex; justify-content: space-between; align-items: center; gap: 10px; padding: 0 12px; }
  .card-front .brand { font-size: 13px; gap: 6px; }
  .card-front .brand-dot { width: 9px; height: 9px; }
  .card-front .contact { color: var(--blue); font-size: 6px; line-height: 1.5; }
  .card-back { left: 320px; background: linear-gradient(135deg, var(--teal), var(--cyan) 60%, var(--blue)); display: flex; align-items: center; justify-content: center; }
  .card-back .brand { color: #fff; font-size: 18px; }
  .card-back .brand-dot { width: 13px; height: 13px; background: #fff; }

  /* Disc */
  .disc { position: absolute; left: 40px; top: 560px; width: 250px; height: 250px; }
  .disc-label { position: absolute; inset: 0; display: flex; flex-direction: column; align-items: center; justify-content: center; gap: 86px; }
  .disc .brand { font-size: 16px; }
  .disc .brand-dot { width: 11px; height: 11px; }
  .disc .url { font-size: 7.5px; color: #cfd1d4; }

  /* Presentation folder */
  .folder { left: 320px; top: 560px; width: 270px; height: 382px; display: flex; flex-direction: column; }
  .folder .top { height: 92px; }
  .folder .cover { flex: 1; display: flex; align-items: center; justify-content: center; }
  .folder .brand { font-size: 22px; }
  .folder .brand-dot { width: 16px; height: 16px; }
  .folder .blocks { display: flex; height: 34px; }
  .folder .blocks span { flex: 1; }
  .folder .block-teal { background: var(--teal); }
  .folder .block-blue { background: var(--blue); }
  .folder .block-cyan { background: var(--cyan); }
  .folder .bottom { height: 70px; }
</style>
</head>
<body>

<section class="piece slip">
  <div class="stripe"><span class="s1"></span><span class="s2"></span><span class="s3"></span></div>
  <div class="band head">
    <div class="brand"><span class="brand-dot"></span>Ridgemoor</div>
    <div class="script">With Compliments</div>
  </div>
  <div class="field"></div>
  <div class="band foot">www.ridgemoorholdings-example.com.au</div>
</section>

<section class="piece card card-front">
  <div class="band head">
    <div class="name">Your Name Here</div>
    <div class="role">Designation</div>
  </div>
  <div class="body">
    <div class="brand"><span class="brand-dot"></span>Ridgemoor</div>
    <div class="contact">
      Harlow Bay Phone: 07 40551926<br>
      Tessford Phone: 07 40613847<br>
      Mobile: 0491 570 384<br>
      Fax: 07 40338172<br>
      Email: admin@ridgemoorholdings-example.com.au<br>
      ABN 51 824 306 917
    </div>
  </div>
  <div class="stripe"><span class="s1"></span><span class="s2"></span><span class="s3"></span></div>
</section>

<section class="piece card card-back">
  <div class="brand"><span class="brand-dot"></span>Ridgemoor</div>
</section>

<section class="disc">
  <svg width="250" height="250" viewBox="0 0 250 250" aria-hidden="true">
    <circle cx="125" cy="125" r="122" fill="#d9dbde"/>
    <circle cx="125" cy="125" r="116" fill="#39393d"/>
    <circle cx="125" cy="125" r="26" fill="#e6e8eb"/>
    <circle cx="125" cy="125" r="18" fill="#ffffff" stroke="#c4c6c9" stroke-width="2"/>
    <circle cx="125" cy="125" r="9" fill="#e6e8eb"/>
  </svg>
  <div class="disc-label">
    <div class="brand"><span class="brand-dot"></span>Ridgemoor</div>
    <div class="url">www.ridgemoorholdings-example.com.au</div>
  </div>
</section>

<section class="piece folder">
  <div class="band top"></div>
  <div class="stripe"><span class="s1"></span><span class="s2"></span><span class="s3"></span></div>
  <div class="cover">
    <div class="brand"><span class="brand-dot"></span>Ridgemoor</div>
  </div>
  <div class="blocks">
    <span class="block-teal"></span>
    <span class="block-blue"></span>
    <span class="block-cyan"></span>
  </div>
  <div class="band bottom"></div>
</section>

<article class="piece letterhead">
  <div class="stripe"><span class="s1"></span><span class="s2"></span><span class="s3"></span></div>
  <header class="band head">
    <div class="brand"><span class="brand-dot"></span>Ridgemoor</div>
    <div class="contact">
      Harlow Bay Phone: 07 40551926<br>
      Tessford Phone: 07 40613847<br>
      Mobile: 0491 570 384<br>
      Fax: 07 40338172<br>
      Email: admin@ridgemoorholdings-example.com.au<br>
      ABN 51 824 306 917
    </div>
  </header>
  <div class="letter-body">
    <div class="greeting">Hello,</div>
    <p>Lorem Ipsum is simply dummy text of the printing and typesetting industry. Lorem Ipsum has been the industry's standard dummy text ever since the 1500s, when an unknown printer took a galley of type and scrambled it to make a type specimen book. It has survived not only five centuries, but also the leap into electronic typesetting, remaining essentially unchanged. It was popularised in the 1960s with the release of sheets containing Lorem Ipsum passages, and more recently with desktop publishing software including versions of Lorem Ipsum.</p>
    <p>Lorem Ipsum is simply dummy text of the printing and typesetting industry. It has been the industry's standard dummy text ever since the 1500s, when an unknown printer took a galley of type and scrambled it to make a type specimen book. It has survived not only five centuries, but also the leap into electronic typesetting, remaining essentially unchanged.</p>
    <div class="sign-off">Regards,<br>Alex Marlow</div>
    <div class="signature" role="img" aria-label="Handwritten signature"></div>
  </div>
  <footer class="band foot">www.ridgemoorholdings-example.com.au</footer>
</article>

</body>
</html>
```